Trailer Lettering or Partial Wrap

I purchased a new gloss black 7' wide x 12' long x 7' height enclosed cargo trailer that I would like to brand for advertising. on all 4 sides. Our font is AgencyFB (and we only use lower case letters). To reduce cost I thought using the black gloss background could be achieved and use cut out vinyl rather than full wrap unless there are some other ideas. Our colors are Black, White, and Red (HEX #BE1E2D. Items to be displayed:
- logo
- phone # (405) 555-0172
- email. catering@thekoifinok.com
- web address: www.thekoifinok.com
- our 2 restaurant locations
- "Edmond" 4587 SE 62nd, Edmond OK 73019
- "NW-OKC" 2815 E Juniper Ln, Oklahoma City, OK 73148

we would also like to highlight 3 services we offer:
- Catering
- Rent-A-Chef Events
- Sushi Making Classes

For reference our chopsticks from the logo files we use on a lot of print items. Not that I want it to be like this, but I did attach a sample of what ChatGPT created though is in an unusable format and fonts aren't consistent. As well a recent 2' x 4' sign we had made to use on table displays.

We also do like the wording on that last item of " Sushi | Experience | Elevated"

```html
<!DOCTYPE html>
<html lang="en">
<head>
<meta charset="utf-8">
<title>the koi fin — trailer lettering</title>
<link rel="stylesheet" href="https://fonts.googleapis.com/css2?family=Saira+Condensed:wght@300;400;600;700&family=Saira+Extra+Condensed:wght@500;600&display=swap">
<style>
  :root {
    --bg: #e9eaec;
    --panel: #0d0d0e;
    --frame: #b9bcc0;
    --red: #be1e2d;
    --pink: #e8485e;
    --white: #ffffff;
    --muted: #d8d8d8;
  }
  * { box-sizing: border-box; margin: 0; padding: 0; }
  html, body { width: 821px; height: 1200px; overflow: hidden; }
  body {
    background: var(--bg);
    position: relative;
    font-family: "Saira Condensed", "Arial Narrow", sans-serif;
    color: var(--white);
  }
  .panel { position: absolute; background: var(--panel); overflow: hidden; }
  .panel--side { left: 20px; top: 20px; width: 781px; height: 480px; }
  .panel--rear { left: 200px; top: 530px; width: 420px; height: 650px; }
  .abs { position: absolute; }

  .brand-name {
    font-family: "Saira Extra Condensed", "Arial Narrow", sans-serif;
    font-weight: 600;
    color: var(--red);
    line-height: 0.86;
    letter-spacing: -1px;
  }
  .panel--side .brand-name { left: 44px; top: 30px; font-size: 112px; }
  .panel--rear .brand-name { left: 34px; top: 120px; font-size: 160px; }

  .web-band { display: block; }
  .web-text {
    font-weight: 700; color: var(--white); white-space: nowrap;
    letter-spacing: 0.2px;
  }
  .panel--side .web-text { left: 300px; top: 66px; font-size: 20px; }
  .panel--rear .web-text { left: 70px; top: 42px; font-size: 24px; }

  .services { left: 265px; top: 155px; width: 250px; }
  .service { display: flex; align-items: center; height: 44px; }
  .service__icon { width: 36px; height: 36px; flex: none; margin-right: 8px; }
  .service__label { font-weight: 300; font-size: 27px; line-height: 1; }
  .service-rule { height: 1px; background: var(--red); margin-left: 44px; }

  .contact { display: flex; align-items: center; white-space: nowrap; }
  .contact__icon { width: 30px; height: 30px; flex: none; margin-right: 5px; }
  .contact__text { font-weight: 600; font-size: 24px; }
  .panel--side .contact--phone { left: 68px; top: 346px; }
  .panel--side .contact--email { left: 250px; top: 346px; }
  .panel--rear .contact--phone { left: 40px; top: 560px; }
  .panel--rear .contact--email { left: 40px; top: 600px; }

  .door { left: 535px; top: 66px; width: 215px; height: 404px; border: 6px solid var(--frame); }
  .location { width: 100%; text-align: center; font-weight: 300; font-size: 16px; line-height: 1.1; }
  .location__pin { width: 26px; height: 38px; display: block; margin: 0 auto 10px; }
  .location__name { font-weight: 600; font-size: 17px; }
  .location--edmond { top: 44px; }
  .location--okc { top: 164px; }
</style>
</head>
<body>

  <!-- side of trailer -->
  <section class="panel panel--side">
    <div class="abs brand-name">the<br>koi<br>fin</div>

    <svg class="abs web-band" style="left:268px;top:55px" width="252" height="46" role="img" aria-label="red brush stroke behind web address">
      <rect x="0" y="4" width="252" height="38" rx="10" fill="var(--pink)"/>
    </svg>
    <div class="abs web-text">www.thekoifinok.com</div>

    <div class="abs services">
      <div class="service">
        <svg class="service__icon" viewBox="0 0 36 36"><circle cx="18" cy="18" r="16" fill="none" stroke="var(--red)" stroke-width="2"/><rect x="10" y="14" width="16" height="9" rx="2" fill="none" stroke="var(--white)" stroke-width="1.5"/><line x1="10" y1="18" x2="26" y2="18" stroke="var(--white)" stroke-width="1.2"/></svg>
        <span class="service__label">catering</span>
      </div>
      <div class="service-rule"></div>
      <div class="service">
        <svg class="service__icon" viewBox="0 0 36 36"><circle cx="18" cy="18" r="16" fill="none" stroke="var(--red)" stroke-width="2"/><path d="M12 17a4 4 0 0 1 3-6a4 4 0 0 1 7 0a4 4 0 0 1 3 6v7h-13z" fill="none" stroke="var(--white)" stroke-width="1.5"/></svg>
        <span class="service__label">rent-a-chef events</span>
      </div>
      <div class="service-rule"></div>
      <div class="service">
        <svg class="service__icon" viewBox="0 0 36 36"><circle cx="18" cy="18" r="16" fill="none" stroke="var(--red)" stroke-width="2"/><path d="M11 16h14l-2 10h-10z" fill="none" stroke="var(--white)" stroke-width="1.5"/><line x1="20" y1="15" x2="25" y2="8" stroke="var(--white)" stroke-width="1.3"/></svg>
        <span class="service__label">sushi making classes</span>
      </div>
    </div>

    <svg class="abs" style="left:66px;top:328px" width="452" height="10">
      <line x1="2" y1="5" x2="442" y2="5" stroke="var(--red)" stroke-width="2.5" stroke-dasharray="0.1 5" stroke-linecap="round"/>
      <path d="M442 1l8 4l-8 4z" fill="var(--red)"/>
    </svg>

    <div class="abs contact contact--phone">
      <svg class="contact__icon" viewBox="0 0 30 30"><circle cx="15" cy="15" r="13" fill="none" stroke="var(--red)" stroke-width="2"/><path d="M9 13c0-3 12-3 12 0l-2 1c-1-2-7-2-8 0zM11 15h8l1 6h-10z" fill="var(--red)"/></svg>
      <span class="contact__text">(405) 555-0172</span>
    </div>
    <div class="abs contact contact--email">
      <svg class="contact__icon" viewBox="0 0 30 30"><circle cx="15" cy="15" r="13" fill="none" stroke="var(--red)" stroke-width="2"/><rect x="8" y="10" width="14" height="10" fill="none" stroke="var(--red)" stroke-width="1.6"/><path d="M8 10l7 6l7-6" fill="none" stroke="var(--red)" stroke-width="1.6"/></svg>
      <span class="contact__text">catering@thekoifinok.com</span>
    </div>

    <div class="abs door">
      <div class="abs location location--edmond">
        <svg class="location__pin" viewBox="0 0 26 38"><path d="M13 0a13 13 0 0 1 13 13c0 10-13 25-13 25S0 23 0 13A13 13 0 0 1 13 0z" fill="var(--red)"/><circle cx="13" cy="13" r="5" fill="var(--panel)"/></svg>
        <div class="location__name">"Edmond"</div>
        <div>4587 SE 62nd</div>
        <div>Edmond OK</div>
        <div>73019</div>
      </div>
      <div class="abs location location--okc">
        <svg class="location__pin" viewBox="0 0 26 38"><path d="M13 0a13 13 0 0 1 13 13c0 10-13 25-13 25S0 23 0 13A13 13 0 0 1 13 0z" fill="var(--red)"/><circle cx="13" cy="13" r="5" fill="var(--panel)"/></svg>
        <div class="location__name">"NW-OKC"</div>
        <div>2815 E Juniper Ln,</div>
        <div>Oklahoma City, OK</div>
        <div>73148</div>
      </div>
    </div>
  </section>

  <!-- rear doors -->
  <section class="panel panel--rear">
    <svg class="abs web-band" style="left:30px;top:28px" width="360" height="56" role="img" aria-label="red brush stroke behind web address">
      <rect x="0" y="4" width="360" height="48" rx="12" fill="var(--pink)"/>
    </svg>
    <div class="abs web-text">www.thekoifinok.com</div>

    <div class="abs brand-name">the<br>koi<br>fin</div>

    <svg class="abs" style="left:36px;top:535px" width="352" height="10">
      <line x1="2" y1="5" x2="342" y2="5" stroke="var(--red)" stroke-width="2.5" stroke-dasharray="0.1 5" stroke-linecap="round"/>
      <path d="M342 1l8 4l-8 4z" fill="var(--red)"/>
    </svg>

    <div class="abs contact contact--phone">
      <svg class="contact__icon" viewBox="0 0 30 30"><circle cx="15" cy="15" r="13" fill="none" stroke="var(--red)" stroke-width="2"/><path d="M9 13c0-3 12-3 12 0l-2 1c-1-2-7-2-8 0zM11 15h8l1 6h-10z" fill="var(--red)"/></svg>
      <span class="contact__text">(405) 555-0172</span>
    </div>
    <div class="abs contact contact--email">
      <svg class="contact__icon" viewBox="0 0 30 30"><circle cx="15" cy="15" r="13" fill="none" stroke="var(--red)" stroke-width="2"/><rect x="8" y="10" width="14" height="10" fill="none" stroke="var(--red)" stroke-width="1.6"/><path d="M8 10l7 6l7-6" fill="none" stroke="var(--red)" stroke-width="1.6"/></svg>
      <span class="contact__text">catering@thekoifinok.com</span>
    </div>
  </section>

</body>
</html>
```